Halt and Thicken New Branding Stationary Set - updated Oct 30th 2017

Updated on 30th Oct 2017 as we now need a whole folder design instead of a folder cover. We have thought out exactly what should be on it so it wont be hard. We are happy for this to be completed only by the winning designer if you like. And also we are guaranteeing this project now. Thanks!

We just got our new logo and now we would like a stationary set so we can brand our company communications. The items we need designed are:
Business cards
Letterhead
Appointment confirmation cards
Folder - switched from folder cover. Note that if you don't wish to do this unless you are selected as the winner this is fine.

1. Business cards - for 5 employees, final names will be given once the winner is selected, but you can use this one as the sample:
Lucinda Prieto
Hair Regrowth Expert
Halt and Thicken
7127 Marbury Ave, Suite 500
Kestrel Park CA 90877
lucinda@gavinthorpemd.example
(555) 238-9016

2. Letterhead 8.5" x 11.0" vertical
Halt and Thicken
Kestrel Park CA 90877
office@haltandthicken.example
(555) 238-9016

3. Appointment Confirmation cards - business card size
Halt and Thicken
Kestrel Park CA 90877
Appointment For:
Date:
Time:
If you are unable to make your appointment, please contact us to reschedule at:
(555) 238-9016
info@gavinthorpemd.example

*UPDATED*
4. Folder 9" x 12 " vertical with double pocket
We would like the infinity image from the logo made really big so the left side is on the back and the right side with the + sign is on the front and its takes up the maximum room on the folder.
On the front below the half logo it should say "A Biochemical Revolution..."
On the inside we would also like to have the infinity sign from the logo but faded and half on the left pocket half on the right.
On left inside pocket it should say (this will be partically written on top of the logo):
Gavin Thorpe MD
Precision Medicine
Halt and Thicken Hair
On the Right inside pocket it should say the following:
Because the Enemy of BETTER Health is Good Health
BETTER Ingredients
BETTER Recipe
BETTER Medicine
On the back below the logo on the bottom should be the contact information.
I attached a picture of our drawing of what we want for this to make it easier.

Here is our website to give you an idea of our branding: http://www.haltandthicken.example/

We are the only true cure for hair loss and need to look professional and highest quality and beyond reproach from an ethical standpoint. We are a medical clinic so this should be portrayed also.
We cured hair loss by analyzing biochemistry and rebalancing it so that the process reverses and your own hair can grow back naturally.

Business card information:

OK so here is the information for the business cards:

Lucinda Prieto
Hair Regrowth Expert
(555) 238-9016
www.haltandthicken.example

Marisol Quintero
Hair Growth Consultant
(555) 238-9016
marisol@gavinthorpemd.example
www.haltandthicken.example

Glenda Hutchins
CMO/COO
(555) 238-9016
glenda@haltandthicken.example
www.haltandthicken.example

Dr Lou Thorpe
President
(555) 238-9016
info@gavinthorpemd.example
www.haltandthicken.example

Halt and Thicken
Customer Service
(555) 238-9016
info@gavinthorpemd.example
www.haltandthicken.example

Target Market(s)

Men aged 20-24 who care about their appearance, care about their hair and care about the world.

Industry/Entity Type

Medical And Science

Font styles to use
Sans Serif

Colors
00a990
ffffff
9d9d9d
333333

Requirements
Must have
• Must use the logo and our brand colors from the logo in all designs.
• The pantone colors are:
• Green: #4ca26f
• Light Grey: #999999
• The design should be symmetrical and balanced.
Nice to have
• It should look reasonably masculine.
Should not have
• Do not include any red in the design.

```html
<!DOCTYPE html>
<html lang="en">
<head>
<meta charset="utf-8">
<title>Appointment Card – Halt and Thicken</title>
<link rel="stylesheet" href="https://fonts.googleapis.com/css2?family=Open+Sans:wght@400;600;700&family=Handlee&display=swap">
<style>
  :root {
    --brand-green: #4ca26f;
    --frame-green: #d6eadd;
    --label-grey: #6a6a6a;
    --body-grey: #5a5a5a;
    --dark-grey: #333333;
    --ink-blue: #2b5ea6;
    --rule-grey: #b9b9b9;
    --paper: #ffffff;
  }
  html, body {
    margin: 0;
    padding: 0;
    width: 1200px;
    height: 708px;
    overflow: hidden;
    background: var(--paper);
  }
  .appointment-card {
    position: relative;
    width: 1200px;
    height: 708px;
    box-sizing: border-box;
    border: 3px solid var(--frame-green);
    background: var(--paper);
    font-family: "Open Sans", Arial, sans-serif;
    color: var(--body-grey);
  }
  .card-heading {
    position: absolute;
    left: 57px;
    top: 68px;
    margin: 0;
    font-size: 44px;
    font-weight: 700;
    color: var(--brand-green);
    letter-spacing: -0.3px;
  }
  .field {
    position: absolute;
    left: 105px;
    display: flex;
    align-items: baseline;
    width: 660px;
  }
  .field--for { top: 196px; }
  .field--date { top: 286px; }
  .field--time { top: 374px; }
  .field-label {
    width: 125px;
    font-size: 35px;
    color: var(--label-grey);
  }
  .field-value {
    flex: 1;
    font-family: "Handlee", cursive;
    font-size: 33px;
    color: var(--ink-blue);
    border-bottom: 2px dashed var(--rule-grey);
    padding-bottom: 2px;
    white-space: nowrap;
  }
  .reschedule-note {
    position: absolute;
    left: 59px;
    top: 502px;
    margin: 0;
    font-size: 29px;
    line-height: 44px;
    color: var(--body-grey);
  }
  .reschedule-note .contact-line {
    color: var(--dark-grey);
  }
  .brand-mark {
    position: absolute;
    right: 60px;
    top: 462px;
    display: flex;
    align-items: center;
    gap: 12px;
  }
  .brand-dot {
    width: 26px;
    height: 26px;
    border-radius: 50%;
    background: var(--brand-green);
  }
  .brand-name {
    font-size: 28px;
    font-weight: 600;
    color: var(--brand-green);
  }
  .clinic-address {
    position: absolute;
    right: 54px;
    top: 514px;
    margin: 0;
    text-align: right;
    font-style: normal;
    font-size: 29px;
    line-height: 44px;
    color: var(--body-grey);
  }
</style>
</head>
<body>
  <main class="appointment-card">
    <h1 class="card-heading">We look forward to seeing you!</h1>

    <div class="field field--for">
      <span class="field-label">For:</span>
      <span class="field-value">Hair regrowth consultation</span>
    </div>
    <div class="field field--date">
      <span class="field-label">Date:</span>
      <span class="field-value">Monday, 26th April, 2018</span>
    </div>
    <div class="field field--time">
      <span class="field-label">Time:</span>
      <span class="field-value">10:00 AM</span>
    </div>

    <p class="reschedule-note">
      If you are unable to make your appointment,<br>
      please contact us to reschedule at:<br>
      <span class="contact-line">(555) 238-9016 &nbsp;or&nbsp; info@gavinthorpemd.example</span>
    </p>

    <div class="brand-mark">
      <span class="brand-dot"></span>
      <span class="brand-name">Halt and Thicken</span>
    </div>

    <address class="clinic-address">
      7127 Marbury Ave<br>
      Suite 500, Kestrel Park<br>
      California 90877
    </address>
  </main>
</body>
</html>
```